Spring ORVu 2016 Training Weekend Program Booklet

We need graphic design for the program booklet for our Spring leadership development training weekend for minority MBA students working in Finance. The design should include the colors in the attached logo and be fun and young (but somewhat conservative). The final files should be either Adobe InDesign or Illustrator so we can lay in text and images as needed. The layout will be:
Front Cover
Interior Page Template with Design
Inside Front Cover - Table of Contents
Page 1. Welcome Letter
Pages 2-3. Sponsor Acknowledgement
Pages 4-5. Program Agenda
Page 6. Listing of speakers and presenters
Page 7. Upcoming Events (Calendar)
Pages 8-10 Student Directory
Page 11. Listing of School Captains
Page 12. Resource Documents (title page)
Pages 13-16 Resource Documents
Pages 17 - 24. Notes Pages (blank for taking notes)
A sample of last season's book is provided.
Target Market(s)
Minority business school students attending top business schools (i.e Penmoor, Dunstry, Calbrook, etc.)
Industry/Entity Type
Financial Service

```html
<!DOCTYPE html>
<html lang="en">
<head>
<meta charset="utf-8">
<title>Student Directory</title>
<link href="https://fonts.googleapis.com/css2?family=Source+Sans+3:wght@400;600;700&display=swap" rel="stylesheet">
<style>
  :root {
    --spread-blue: #3f87b8;
    --spread-blue-deep: #2d6f9f;
    --spread-blue-light: #6aa6cf;
    --band-green: #cdd596;
    --ink: #1b1b1b;
    --paper: #ffffff;
  }
  * { margin: 0; padding: 0; box-sizing: border-box; }
  html, body {
    width: 1200px;
    height: 776px;
    overflow: hidden;
    background: var(--paper);
  }
  .spread {
    position: relative;
    width: 1200px;
    height: 776px;
    overflow: hidden;
    font-family: "Source Sans 3", "Myriad Pro", Arial, sans-serif;
  }
  .spread__art {
    position: absolute;
    inset: 0;
    width: 1200px;
    height: 776px;
  }
  .section-title {
    position: absolute;
    left: 0;
    top: 62px;
    width: 441px;
    height: 35px;
    background: var(--band-green);
    color: var(--paper);
    font-weight: 600;
    font-size: 23px;
    letter-spacing: 0.2px;
    line-height: 35px;
    padding-left: 35px;
  }
  .directory-column {
    position: absolute;
    top: 121px;
    width: 200px;
    list-style: none;
    color: var(--ink);
    font-size: 8.8px;
    line-height: 11.76px;
  }
  .directory-column--light { color: var(--paper); }
  .directory-column--1 { left: 35px; }
  .directory-column--2 { left: 306px; }
  .directory-column--3 { left: 635px; }
  .directory-column--4 { left: 906px; }
  .category { margin-bottom: 11.8px; }
  .category__name, .category__listing { display: block; height: 11.76px; }
  .category__name { font-weight: 700; }
  .category__listing { font-weight: 400; }
  .page-number {
    position: absolute;
    top: 752px;
    font-size: 7px;
    line-height: 9px;
    color: var(--ink);
  }
  .page-number--left { left: 35px; }
  .page-number--right { left: 1156px; }
</style>
</head>
<body>
<main class="spread">
  <svg class="spread__art" viewBox="0 0 1200 776">
    <defs>
      <linearGradient id="photoTone" x1="0" y1="0" x2="1" y2="1">
        <stop offset="0" stop-color="#6aa6cf"/>
        <stop offset="0.55" stop-color="#3f87b8"/>
        <stop offset="1" stop-color="#2d6f9f"/>
      </linearGradient>
      <linearGradient id="ovalTone" x1="0" y1="0" x2="1" y2="1">
        <stop offset="0" stop-color="#ffffff" stop-opacity="0.8"/>
        <stop offset="1" stop-color="#f3ede4" stop-opacity="0.62"/>
      </linearGradient>
    </defs>
    <rect class="photo-fill" x="0" y="0" width="1200" height="776" fill="url(#photoTone)" role="img" aria-label="Group photo of the training weekend students posing in a bright atrium, tinted blue"/>
    <ellipse class="highlight-oval" cx="445" cy="370" rx="545" ry="300" transform="rotate(-29 445 370)" fill="url(#ovalTone)"/>
  </svg>

  <h1 class="section-title">STUDENT DIRECTORY</h1>

  <ul class="directory-column directory-column--1">
    <li class="category"><span class="category__name">CATEGORY</span><span class="category__listing">Listing</span><span class="category__listing">Listing</span><span class="category__listing">Listing</span><span class="category__listing">Listing</span><span class="category__listing">Listing</span><span class="category__listing">Listing</span><span class="category__listing">Listing</span></li>
    <li class="category"><span class="category__name">CATEGORY</span><span class="category__listing">Listing</span><span class="category__listing">Listing</span><span class="category__listing">Listing</span><span class="category__listing">Listing</span><span class="category__listing">Listing</span><span class="category__listing">Listing</span><span class="category__listing">Listing</span></li>
    <li class="category"><span class="category__name">CATEGORY</span><span class="category__listing">Listing</span><span class="category__listing">Listing</span><span class="category__listing">Listing</span><span class="category__listing">Listing</span><span class="category__listing">Listing</span><span class="category__listing">Listing</span><span class="category__listing">Listing</span></li>
    <li class="category"><span class="category__name">CATEGORY</span><span class="category__listing">Listing</span><span class="category__listing">Listing</span><span class="category__listing">Listing</span><span class="category__listing">Listing</span><span class="category__listing">Listing</span><span class="category__listing">Listing</span><span class="category__listing">Listing</span></li>
    <li class="category"><span class="category__name">CATEGORY</span><span class="category__listing">Listing</span><span class="category__listing">Listing</span><span class="category__listing">Listing</span><span class="category__listing">Listing</span><span class="category__listing">Listing</span><span class="category__listing">Listing</span><span class="category__listing">Listing</span></li>
    <li class="category"><span class="category__name">CATEGORY</span><span class="category__listing">Listing</span><span class="category__listing">Listing</span><span class="category__listing">Listing</span><span class="category__listing">Listing</span><span class="category__listing">Listing</span></li>
  </ul>

  <ul class="directory-column directory-column--2">
    <li class="category"><span class="category__name">CATEGORY</span><span class="category__listing">Listing</span><span class="category__listing">Listing</span><span class="category__listing">Listing</span><span class="category__listing">Listing</span><span class="category__listing">Listing</span><span class="category__listing">Listing</span><span class="category__listing">Listing</span></li>
    <li class="category"><span class="category__name">CATEGORY</span><span class="category__listing">Listing</span><span class="category__listing">Listing</span><span class="category__listing">Listing</span><span class="category__listing">Listing</span><span class="category__listing">Listing</span><span class="category__listing">Listing</span><span class="category__listing">Listing</span></li>
    <li class="category"><span class="category__name">CATEGORY</span><span class="category__listing">Listing</span><span class="category__listing">Listing</span><span class="category__listing">Listing</span><span class="category__listing">Listing</span><span class="category__listing">Listing</span><span class="category__listing">Listing</span><span class="category__listing">Listing</span></li>
    <li class="category"><span class="category__name">CATEGORY</span><span class="category__listing">Listing</span><span class="category__listing">Listing</span><span class="category__listing">Listing</span><span class="category__listing">Listing</span><span class="category__listing">Listing</span><span class="category__listing">Listing</span><span class="category__listing">Listing</span></li>
    <li class="category"><span class="category__name">CATEGORY</span><span class="category__listing">Listing</span><span class="category__listing">Listing</span><span class="category__listing">Listing</span><span class="category__listing">Listing</span><span class="category__listing">Listing</span><span class="category__listing">Listing</span><span class="category__listing">Listing</span></li>
    <li class="category"><span class="category__name">CATEGORY</span><span class="category__listing">Listing</span><span class="category__listing">Listing</span><span class="category__listing">Listing</span><span class="category__listing">Listing</span><span class="category__listing">Listing</span></li>
  </ul>

  <ul class="directory-column directory-column--3">
    <li class="category"><span class="category__name">CATEGORY</span><span class="category__listing">Listing</span><span class="category__listing">Listing</span><span class="category__listing">Listing</span><span class="category__listing">Listing</span><span class="category__listing">Listing</span><span class="category__listing">Listing</span><span class="category__listing">Listing</span></li>
    <li class="category"><span class="category__name">CATEGORY</span><span class="category__listing">Listing</span><span class="category__listing">Listing</span><span class="category__listing">Listing</span><span class="category__listing">Listing</span><span class="category__listing">Listing</span><span class="category__listing">Listing</span><span class="category__listing">Listing</span></li>
    <li class="category"><span class="category__name">CATEGORY</span><span class="category__listing">Listing</span><span class="category__listing">Listing</span><span class="category__listing">Listing</span><span class="category__listing">Listing</span><span class="category__listing">Listing</span><span class="category__listing">Listing</span><span class="category__listing">Listing</span></li>
    <li class="category"><span class="category__name">CATEGORY</span><span class="category__listing">Listing</span><span class="category__listing">Listing</span><span class="category__listing">Listing</span><span class="category__listing">Listing</span><span class="category__listing">Listing</span><span class="category__listing">Listing</span><span class="category__listing">Listing</span></li>
    <li class="category"><span class="category__name">CATEGORY</span><span class="category__listing">Listing</span><span class="category__listing">Listing</span><span class="category__listing">Listing</span><span class="category__listing">Listing</span><span class="category__listing">Listing</span><span class="category__listing">Listing</span><span class="category__listing">Listing</span></li>
    <li class="category"><span class="category__name">CATEGORY</span><span class="category__listing">Listing</span><span class="category__listing">Listing</span><span class="category__listing">Listing</span><span class="category__listing">Listing</span><span class="category__listing">Listing</span></li>
  </ul>

  <ul class="directory-column directory-column--4 directory-column--light">
    <li class="category"><span class="category__name">CATEGORY</span><span class="category__listing">Listing</span><span class="category__listing">Listing</span><span class="category__listing">Listing</span><span class="category__listing">Listing</span><span class="category__listing">Listing</span><span class="category__listing">Listing</span><span class="category__listing">Listing</span></li>
    <li class="category"><span class="category__name">CATEGORY</span><span class="category__listing">Listing</span><span class="category__listing">Listing</span><span class="category__listing">Listing</span><span class="category__listing">Listing</span><span class="category__listing">Listing</span><span class="category__listing">Listing</span><span class="category__listing">Listing</span></li>
    <li class="category"><span class="category__name">CATEGORY</span><span class="category__listing">Listing</span><span class="category__listing">Listing</span><span class="category__listing">Listing</span><span class="category__listing">Listing</span><span class="category__listing">Listing</span><span class="category__listing">Listing</span><span class="category__listing">Listing</span></li>
    <li class="category"><span class="category__name">CATEGORY</span><span class="category__listing">Listing</span><span class="category__listing">Listing</span><span class="category__listing">Listing</span><span class="category__listing">Listing</span><span class="category__listing">Listing</span><span class="category__listing">Listing</span><span class="category__listing">Listing</span></li>
    <li class="category"><span class="category__name">CATEGORY</span><span class="category__listing">Listing</span><span class="category__listing">Listing</span><span class="category__listing">Listing</span><span class="category__listing">Listing</span><span class="category__listing">Listing</span><span class="category__listing">Listing</span><span class="category__listing">Listing</span></li>
    <li class="category"><span class="category__name">CATEGORY</span><span class="category__listing">Listing</span><span class="category__listing">Listing</span><span class="category__listing">Listing</span><span class="category__listing">Listing</span><span class="category__listing">Listing</span></li>
  </ul>

  <div class="page-number page-number--left">9</div>
  <div class="page-number page-number--right">10</div>
</main>
</body>
</html>
```